Building company buisness cards

We are looking for a sharp modern new look for our business cards.
We are a New Zealand based company that specialises in house and land packages.
We have attached a photo of the current logo and would like to see if it can be improved somehow if needed.
We are open to any colours but we have chosen green at this stage.
Feel free to change the font and make the logo smarter looking.
Play with the colours and see what looks best.

We want a card that looks so good know one will want to throw it away!

Target Market(s)

Home buyers

Industry/Entity Type

Building

Contact Information for Business Card

Dorian Keswick
0217392604
dkeswick@tidewellhomecraft.co.nz
tidewellhomecraft.co.nz

Font styles to use
Serif
Sans Serif

Colors

Designer to choose colors to be used in the design.

Requirements
Must have
• Logo and company name on one side, details on the other side
Nice to have
• Color codes for the original green are HEX #4a8028, RGB(74,128,40), CMYK(42,0,69,50)
• Round corners, Raised and/or spot UV

```html
<!DOCTYPE html>
<html lang="en">
<head>
<meta charset="utf-8">
<title>Tidewell Homecraft — Business Cards</title>
<link href="https://fonts.googleapis.com/css2?family=Montserrat:wght@400;500;600;800&display=swap" rel="stylesheet">
<style>
  :root {
    --brand-green: #4a8028;
    --card-white: #fbfaf6;
    --ink-dark: #3a3a3a;
    --ink-light: #ffffff;
    --backdrop: #e7e4df;
    --rule-green: #8fb577;
  }
  * { box-sizing: border-box; margin: 0; padding: 0; }
  html, body { width: 1200px; height: 800px; overflow: hidden; }
  body {
    background: var(--backdrop);
    font-family: "Montserrat", Arial, sans-serif;
    display: flex;
    align-items: center;
    justify-content: center;
    gap: 60px;
  }
  .card {
    position: relative;
    width: 530px;
    height: 324px;
    border-radius: 6px;
    overflow: hidden;
    box-shadow: 0 6px 18px rgba(0,0,0,0.12);
  }
  .card-front {
    background: var(--brand-green);
    color: var(--ink-light);
    display: flex;
    flex-direction: column;
    align-items: center;
    justify-content: center;
  }
  .wordmark {
    font-weight: 800;
    font-size: 38px;
    letter-spacing: -0.5px;
    line-height: 1;
    white-space: nowrap;
  }
  .card-front .wordmark { color: var(--ink-light); }
  .divider {
    width: 110px;
    height: 1px;
    margin: 20px 0 26px;
  }
  .card-front .divider { background: rgba(255,255,255,0.45); }
  .front-url {
    font-size: 15px;
    font-weight: 500;
    letter-spacing: 0.2px;
  }
  .card-back { background: var(--card-white); }
  .back-brand {
    position: absolute;
    top: 62px;
    left: 0;
    right: 0;
    display: flex;
    flex-direction: column;
    align-items: center;
  }
  .card-back .wordmark { color: var(--brand-green); }
  .card-back .divider { background: var(--rule-green); margin: 16px 0 0; }
  .contact-list {
    position: absolute;
    right: 26px;
    top: 156px;
    list-style: none;
    font-size: 13px;
    line-height: 1.3;
    color: var(--ink-dark);
    white-space: nowrap;
  }
  .contact-list li {
    display: flex;
    align-items: center;
    gap: 6px;
    margin-bottom: 4px;
  }
  .contact-list svg { width: 13px; height: 13px; flex: none; }
  .contact-list .domain { color: var(--brand-green); }
  .person {
    position: absolute;
    left: 56px;
    bottom: 50px;
    white-space: nowrap;
  }
  .person-name {
    font-size: 23px;
    font-weight: 600;
    color: var(--brand-green);
    line-height: 1;
  }
  .person-title {
    font-size: 16px;
    font-weight: 500;
    color: var(--ink-dark);
    text-align: right;
    margin-top: 2px;
  }
  .footer-band {
    position: absolute;
    left: 0;
    right: 0;
    bottom: 0;
    height: 36px;
    background: var(--brand-green);
  }
</style>
</head>
<body>

  <section class="card card-front" aria-label="Card front">
    <div class="wordmark">tidewell homecraft.</div>
    <div class="divider"></div>
    <div class="front-url">www.tidewellhomecraft.co.nz</div>
  </section>

  <section class="card card-back" aria-label="Card back">
    <div class="back-brand">
      <div class="wordmark">tidewell homecraft.</div>
      <div class="divider"></div>
    </div>

    <ul class="contact-list">
      <li>
        <svg viewBox="0 0 16 16" fill="none" stroke="#4a8028" stroke-width="1.6"><path d="M4 1.5l2.5 3-1.5 2a8 8 0 0 0 4.5 4.5l2-1.5 3 2.5-1.5 2.5C7 14 2 9 1.5 3z"/></svg>
        <span>0217392604</span>
      </li>
      <li>
        <svg viewBox="0 0 16 16" fill="none" stroke="#4a8028" stroke-width="1.4"><rect x="1" y="3" width="14" height="10"/><path d="M1 3l7 6 7-6"/></svg>
        <span>dkeswick@tidewellhomecraft.co.nz</span>
      </li>
      <li>
        <svg viewBox="0 0 16 16" fill="none" stroke="#4a8028" stroke-width="1.4"><circle cx="8" cy="8" r="6.5"/><ellipse cx="8" cy="8" rx="3" ry="6.5"/><path d="M1.5 8h13"/></svg>
        <span>www.<span class="domain">tidewellhomecraft.co.nz</span></span>
      </li>
    </ul>

    <div class="person">
      <div class="person-name">Dorian Keswick</div>
      <div class="person-title">Director</div>
    </div>

    <div class="footer-band"></div>
  </section>

</body>
</html>
```